Silver Heron Coffee Bean Labels

We need a label for a new brand of coffee that we are selling in Portland, Oregon (Coffee Capital). Our company has no current online presence but have some great roasting techniques. We will be roasting our own coffee beans from throughout the world and selling them immediately after roasting causing a super fresh and high quality product.

We will be packaging in brown kraft bags: 3 3/8 X 2.5 x 7.75 inches which is standard for coffee beans.

Also notice on that sample the blue section in the middle has the product name. We want to also make it so that there is a consistent area that we can print OVER the label the name or blend of the coffee.

Our company is called Silver Heron Coffee Roasters. We will want to put silverheronroasters.example on the label someplace (we dont have a site yet but will by launch).

We need to incorporate A Silver Heron into the design. No preferences yet on the style of it.

We want to be a super-premium brand. Sort of like MicroBrew beers. We will sell at Farmers Markets, online, and directly into stores. Image is very important to us.

Labels should be about 3" wide and about 3.75" high.. Perhaps higher if a cool design justifies the height. Again we will be using a brown kraft bag (like grocery bag color) as shown on the sample.

SEE ATTACHED SEVERAL INTERESTING DESIGNS

Target Market(s)

Foodies, Yuppie, Coffee Snob

Industry/Entity Type

It Company

Requirements
Must have
• Location for the product Name to go onto it... We want to use the same labels for our full line. Just printing over it something like "Italian Roast" and a line below saying something like "Bold, Nutty Flavor, blah blah"

Should not have
• Clunkey looking old fonts or things that look homemade.

```html
<!DOCTYPE html>
<html lang="en">
<head>
<meta charset="utf-8">
<title>Silver Heron Coffee Bean Labels</title>
<link rel="stylesheet" href="https://fonts.googleapis.com/css2?family=Oswald:wght@600&family=Great+Vibes&family=Arimo:wght@700&family=Tinos:wght@700&family=Dancing+Script:wght@600&display=swap">
<style>
  :root {
    --backdrop: #efe9e2;
    --espresso: #2a1d18;
    --mocha: #5a3523;
    --rust: #8a4a26;
    --gold: #c99a4a;
    --tan: #d9bf95;
    --cream: #f6ecd2;
    --crimson: #8e1b12;
    --deep-red: #6a1410;
    --white: #ffffff;
  }
  * { margin: 0; padding: 0; box-sizing: border-box; }
  html, body { width: 1200px; height: 1006px; overflow: hidden; background: var(--backdrop); }
  .canvas { position: relative; width: 1200px; height: 1006px; }

  .label { position: absolute; top: 153px; width: 440px; height: 700px; overflow: hidden; }
  .label > * { position: absolute; }
  .label-dark { left: 130px; background: radial-gradient(circle at 50% 55%, var(--rust) 0%, var(--mocha) 45%, var(--espresso) 85%); }
  .label-cream { left: 630px; background: repeating-linear-gradient(90deg, #3b2a22 0 18px, #47332a 18px 36px); }

  .badge-shape { left: 0; top: 0; width: 440px; height: 700px; }
  .brand-mark { left: 0; width: 440px; display: flex; justify-content: center; }
  .brand-dot { width: 54px; height: 54px; border-radius: 50%; background: #b8b8b8; }
  .brand-name { left: 0; width: 440px; text-align: center; font-family: "Tinos", serif; font-weight: 700; font-size: 17px; white-space: nowrap; }
  .site { left: 0; width: 440px; text-align: center; font-family: "Arimo", sans-serif; font-size: 9px; white-space: nowrap; }
  .headline { left: 0; width: 440px; text-align: center; font-family: "Oswald", sans-serif; font-weight: 600; font-size: 50px; line-height: 1; letter-spacing: -0.5px; white-space: nowrap; }
  .headline-script { left: 0; width: 440px; text-align: center; font-family: "Great Vibes", cursive; font-size: 62px; line-height: 1; }
  .roast-band { display: flex; align-items: center; justify-content: center; font-family: "Arimo", sans-serif; font-weight: 700; font-size: 27px; white-space: nowrap; }
  .flavor { left: 0; width: 440px; text-align: center; font-family: "Dancing Script", cursive; font-size: 18px; }
  .art { border-radius: 8px; }

  .label-dark .brand-mark { top: 52px; }
  .label-dark .brand-name { top: 150px; color: var(--white); }
  .label-dark .site { top: 174px; color: #cfc3b6; }
  .label-dark .headline { top: 194px; color: var(--tan); }
  .label-dark .headline-script { top: 246px; color: var(--tan); }
  .label-dark .roast-band { left: 85px; top: 330px; width: 270px; height: 46px; background: var(--tan); color: var(--espresso); border-radius: 3px; }
  .label-dark .flavor { top: 388px; color: var(--gold); }
  .label-dark .cup-art { left: 120px; top: 430px; width: 200px; height: 170px; background: linear-gradient(180deg, #4a3024 0%, #8a7466 55%, #d8d2cb 100%); }

  .label-cream .brand-mark { top: 44px; }
  .label-cream .brand-dot { width: 44px; height: 44px; }
  .label-cream .beans-top { left: 90px; top: 34px; width: 260px; height: 100px; background: linear-gradient(180deg, #6b3a1e, #3a1d0e); }
  .label-cream .brand-name { top: 98px; color: var(--white); font-size: 16px; }
  .label-cream .headline { top: 154px; color: var(--crimson); font-size: 46px; }
  .label-cream .headline-script { top: 200px; color: var(--espresso); font-size: 54px; }
  .label-cream .roast-band { left: 80px; top: 272px; width: 280px; height: 42px; background: var(--crimson); color: var(--white); border: 2px solid var(--cream); outline: 2px solid var(--crimson); }
  .label-cream .flavor { top: 326px; color: var(--espresso); font-size: 17px; }
  .label-cream .beans-scatter { left: 60px; top: 362px; width: 320px; height: 60px; background: linear-gradient(180deg, rgba(90,42,20,0), #5a2a14); }
  .label-cream .cup-art { left: 110px; top: 420px; width: 220px; height: 190px; background: linear-gradient(180deg, #3a2418 0%, #9a8f88 50%, #e9e6e2 100%); }
  .label-cream .site { left: 130px; top: 642px; width: 180px; height: 18px; line-height: 18px; background: var(--cream); color: var(--espresso); border-radius: 3px; }
</style>
</head>
<body>
<main class="canvas">

  <section class="label label-dark" aria-label="Dark label">
    <svg class="badge-shape" viewBox="0 0 440 700" aria-hidden="true">
      <path d="M70,30 L370,30 L410,90 L410,540 L370,620 L220,680 L70,620 L30,540 L30,90 Z" fill="var(--espresso)" stroke="var(--gold)" stroke-width="5"/>
      <path d="M80,42 L360,42 L396,96 L396,534 L360,608 L220,664 L80,608 L44,534 L44,96 Z" fill="none" stroke="var(--gold)" stroke-width="1.5" opacity="0.6"/>
      <path d="M70,340 L85,330 L85,376 L70,366 Z M370,340 L355,330 L355,376 L370,366 Z" fill="#b99a6e"/>
    </svg>
    <div class="brand-mark"><span class="brand-dot"></span></div>
    <p class="brand-name">Silver Heron Coffee Roasters</p>
    <p class="site">silverheronroasters.example</p>
    <h1 class="headline">Fresh Roasted</h1>
    <p class="headline-script">Coffee</p>
    <p class="roast-band">Italian Roast</p>
    <p class="flavor">Bold, Nutty Flavor</p>
    <div class="art cup-art" role="img" aria-label="Steaming cup of coffee on a saucer"></div>
  </section>

  <section class="label label-cream" aria-label="Cream label">
    <svg class="badge-shape" viewBox="0 0 440 700" aria-hidden="true">
      <rect x="30" y="18" width="380" height="664" rx="34" fill="var(--cream)" stroke="#d8c39a" stroke-width="3"/>
      <path d="M30,430 Q120,380 220,430 Q320,380 410,430 L410,648 Q410,682 376,682 L64,682 Q30,682 30,648 Z" fill="var(--deep-red)"/>
      <path d="M60,450 Q140,410 220,455 Q300,410 380,450 L380,630 L60,630 Z" fill="var(--crimson)"/>
    </svg>
    <div class="art beans-top" role="img" aria-label="Roasted coffee beans"></div>
    <div class="brand-mark"><span class="brand-dot"></span></div>
    <p class="brand-name">Silver Heron Coffee Roasters</p>
    <h1 class="headline">Fresh Roasted</h1>
    <p class="headline-script">Coffee</p>
    <p class="roast-band">Italian Roast</p>
    <p class="flavor">Bold, Nutty Flavor</p>
    <div class="art beans-scatter" role="img" aria-label="Scattered coffee beans"></div>
    <div class="art cup-art" role="img" aria-label="Cup of black coffee on a saucer with beans"></div>
    <p class="site">silverheronroasters.example</p>
  </section>

</main>
</body>
</html>
```